We want a business card/punch card for our business. We are including examples of our current business card (we like the front of our business card and not looking to remake it). We need only back side to be designed in form of a punch card (we are including a sample of the punch card we made, but are unsatisfied). For each $180 spend (9 punches) our clients have $20 off.

Colors
886aae

```html
<!DOCTYPE html>
<html lang="en">
<head>
<meta charset="UTF-8">
<title>Punch Card – Front and Back</title>
<link rel="stylesheet" href="https://fonts.googleapis.com/css2?family=Gilda+Display&family=Playfair+Display:ital,wght@1,700&display=swap">
<style>
  :root {
    --page: #ffffff;
    --shadow: #b3b3b3;
    --card-light: #ebebeb;
    --brand: #886aae;
    --brand-deep: #77569e;
    --text-violet: #7a5aa8;
    --back-base: #6a4e8c;
    --back-wave: #664a86;
    --back-hill: #503a6a;
    --white: #ffffff;
  }
  html, body {
    margin: 0;
    padding: 0;
    overflow: hidden;
    background: var(--page);
  }
  .canvas {
    position: relative;
    width: 1200px;
    height: 1200px;
    background: var(--page);
  }
  .card-shadow {
    position: absolute;
    background: var(--shadow);
  }
  .card {
    position: absolute;
    width: 805px;
    height: 483px;
    display: block;
  }
  .card--front { left: 206px; top: 89px; }
  .card--back  { left: 201px; top: 618px; }
  .card-shadow--front { left: 191px; top: 105px; width: 811px; height: 481px; }
  .card-shadow--back  { left: 189px; top: 631px; width: 810px; height: 480px; }

  .service-list text {
    font-family: "Gilda Display", serif;
    font-size: 38px;
    fill: var(--text-violet);
  }
  .punch-tile rect { fill: var(--card-light); }
  .punch-tile text {
    font-family: "Playfair Display", serif;
    font-style: italic;
    font-weight: 700;
    font-size: 33px;
    fill: var(--brand);
    text-anchor: middle;
  }
  .reward-note {
    font-family: "Gilda Display", serif;
    font-size: 27px;
    fill: var(--white);
    text-anchor: middle;
  }
</style>
</head>
<body>
<main class="canvas">

  <div class="card-shadow card-shadow--front"></div>
  <svg class="card card--front" viewBox="0 0 1006 604" xmlns="http://www.w3.org/2000/svg" aria-label="Punch card front">
    <rect class="card-base" width="1006" height="604" fill="var(--card-light)"/>
    <path class="wave-light" fill="var(--brand)"
      d="M0,603 C200,520 380,360 520,232 C640,160 720,150 790,132 C880,110 960,70 1006,29 L1006,603 Z"/>
    <path class="wave-hill" fill="var(--brand-deep)"
      d="M0,603 C200,540 360,420 480,350 C540,318 580,312 620,316 C760,330 900,440 1006,603 Z"/>

    <g class="service-list">
      <text x="54" y="101">Tantra</text>
      <text x="54" y="146">Sexual Healing</text>
      <text x="54" y="194">Intomacy Coaching</text>
      <text x="54" y="246">Sound Healing</text>
      <text x="54" y="297">Sound Baths</text>
      <text x="54" y="355">Crystal Healing</text>
      <text x="54" y="407">Yoga</text>
    </g>

    <g class="punch-grid">
      <g class="punch-tile"><rect x="520" y="302" width="80" height="74" rx="8" transform="skewX(-8) translate(42 0)"/><text x="556" y="351">$20</text></g>
      <g class="punch-tile"><rect x="622" y="302" width="80" height="74" rx="8" transform="skewX(-8) translate(42 0)"/><text x="658" y="351">$20</text></g>
      <g class="punch-tile"><rect x="724" y="302" width="80" height="74" rx="8" transform="skewX(-8) translate(42 0)"/><text x="760" y="351">$20</text></g>
      <g class="punch-tile"><rect x="824" y="302" width="80" height="74" rx="8" transform="skewX(-8) translate(42 0)"/><text x="860" y="351">$20</text></g>
      <g class="punch-tile"><rect x="520" y="397" width="80" height="74" rx="8" transform="skewX(-8) translate(56 0)"/><text x="556" y="446">$20</text></g>
      <g class="punch-tile"><rect x="622" y="397" width="80" height="74" rx="8" transform="skewX(-8) translate(56 0)"/><text x="658" y="446">$20</text></g>
      <g class="punch-tile"><rect x="724" y="397" width="80" height="74" rx="8" transform="skewX(-8) translate(56 0)"/><text x="760" y="446">$20</text></g>
      <g class="punch-tile"><rect x="824" y="397" width="80" height="74" rx="8" transform="skewX(-8) translate(56 0)"/><text x="860" y="446">$20</text></g>
    </g>

    <text class="reward-note" x="710" y="522">Filling this cord with 9 punches gives you</text>
    <text class="reward-note" x="710" y="555">$20 off your next visit</text>
  </svg>

  <div class="card-shadow card-shadow--back"></div>
  <svg class="card card--back" viewBox="0 0 1006 604" xmlns="http://www.w3.org/2000/svg" aria-label="Punch card back">
    <rect class="card-base" width="1006" height="604" fill="var(--back-base)"/>
    <path class="wave-mid" fill="var(--back-wave)"
      d="M0,603 C200,520 380,360 520,232 C640,160 720,150 790,132 C880,110 960,70 1006,29 L1006,603 Z"/>
    <path class="wave-hill" fill="var(--back-hill)"
      d="M0,603 C200,540 360,420 480,350 C540,318 580,312 620,316 C760,330 900,440 1006,603 Z"/>
  </svg>

</main>
</body>
</html>
```